Kitchen Tools Infographic - Helpful Items for Healthy Home Meals

We are a weight loss company that provides holistic, natural nutrition programs to consumers -- you can see our web site at www.FernQuill.com. We need a simple infographic to be shared on social media and via email. The topic for the infographic is "Equip Your Kitchen for Healthy Home Meals". We've outlined 5 groups of kitchen tools that are helpful for consumers to have for preparing home meals, and included some framing statistics emphasizing the weight management benefits of preparing meals versus eating out.

Target Market(s)

Women age 35-55

Industry/Entity Type

Health And Wellness

Font styles to use
Sans Serif

Colors
0292cd
9bcb3b

Requirements
Must have
• - FernQuill Logo
• - Graphics summarizing statistic (weight gain)
• - Graphics showing groupings of kitchen tools
Should not have
• body scale graphics
• before/after graphics

```html
<!DOCTYPE html>
<html lang="en">
<head>
<meta charset="utf-8">
<title>Equip Your Kitchen for Healthy Home Meals</title>
<link href="https://fonts.googleapis.com/css2?family=Raleway:wght@300;400;500&family=Oswald:wght@300;400&family=Roboto+Condensed:wght@400&family=Open+Sans:wght@400;600&family=Lora:ital@1&display=swap" rel="stylesheet">
<style>
:root{
  --teal:#0292cd;
  --teal-bright:#10b4d4;
  --teal-dark:#0b7fa6;
  --green:#9bcb3b;
  --green-dark:#7fae2a;
  --ink:#555a5e;
  --ink-soft:#777c80;
  --grey-band:#f2f2f2;
  --grey-foot:#dcdcdc;
  --tab-grey:#e9e9e9;
  --tab-num:#bdbdbd;
  --white:#ffffff;
}
*{margin:0;padding:0;box-sizing:border-box}
html,body{width:1200px;height:2880px;overflow:hidden;background:var(--white)}
body{position:relative;font-family:"Open Sans",Arial,sans-serif;color:var(--ink)}
.abs{position:absolute}
.center{text-align:center}

/* header */
.header{top:0;left:0;width:1200px;height:298px;background:var(--white)}
.title-ribbon{left:280px;top:20px}
.title-main{left:0;width:1200px;top:42px;font-family:"Raleway",sans-serif;font-weight:400;font-size:42px;letter-spacing:1px;color:var(--white)}
.title-for{left:0;width:1200px;top:140px;font-family:"Lora",serif;font-style:italic;font-size:30px;color:var(--ink)}
.title-sub{left:0;width:1200px;top:200px;font-family:"Raleway",sans-serif;font-weight:400;font-size:46px;letter-spacing:1px;color:var(--teal-bright)}

/* why section */
.why{top:298px;left:0;width:1200px;height:754px;background:var(--grey-band)}
.why-heading{left:0;width:1200px;top:55px;font-family:"Raleway",sans-serif;font-weight:500;font-size:29px;color:var(--green)}
.why-text{left:198px;width:806px;top:126px;font-size:17px;line-height:32px;color:var(--ink)}
.chart{top:270px}
.chart-label{font-family:"Roboto Condensed",sans-serif;font-size:15px;fill:var(--ink)}
.chart-ribbon-text{font-family:"Roboto Condensed",sans-serif;font-size:17px;fill:var(--white);letter-spacing:.3px}

/* tools */
.tools-heading{left:0;width:1200px;top:1104px;font-family:"Raleway",sans-serif;font-weight:300;font-size:35px;color:var(--ink)}
.column{top:1196px;width:230px}
.column-head{display:block;margin-left:19px}
.tool{position:absolute;left:0;width:230px;text-align:center}
.tool-icon{display:block;margin:0 auto;width:104px;height:104px;border-radius:12px}
.icon-teal{background:linear-gradient(160deg,#bfe6f3,#5bbfe0)}
.icon-green{background:linear-gradient(160deg,#dcefb5,#a9d455)}
.tool-name{margin-top:26px;font-family:"Roboto Condensed",sans-serif;font-size:16.5px;letter-spacing:.2px;color:var(--teal-bright);text-transform:uppercase;line-height:21px}
.tool-desc{margin-top:10px;font-size:15px;line-height:21px;color:var(--ink)}
.col-num{font-family:"Oswald",sans-serif;font-weight:300;font-size:62px;fill:var(--tab-num)}
.col-word{font-family:"Oswald",sans-serif;font-weight:400;font-size:56px;fill:var(--white)}

/* contact */
.contact{top:2390px;left:0;width:1200px;height:413px;background:var(--grey-band)}
.contact-ribbon{left:280px;top:48px}
.ribbon-text{font-family:"Open Sans",sans-serif;font-size:22px;fill:var(--white)}
.invite{left:0;width:1200px;top:162px;font-size:20px;color:var(--ink)}
.brand{left:0;width:1200px;top:238px;display:flex;justify-content:center;align-items:center;gap:14px}
.brand-dot{width:30px;height:30px;border-radius:50%;background:var(--green)}
.brand-name{font-family:"Open Sans",sans-serif;font-weight:600;font-size:30px;color:var(--teal)}
.site{left:0;width:1200px;top:320px;font-size:21px;color:var(--teal-bright)}

/* sources */
.sources{top:2803px;left:0;width:1200px;height:77px;background:var(--grey-foot);font-size:12.5px;color:var(--ink-soft);line-height:25px;padding:12px 0 0 62px}
.sources span{display:inline-block;width:58px}
</style>
</head>
<body>

<section class="header abs">
  <svg class="title-ribbon abs" width="640" height="120" viewBox="0 0 640 120" aria-hidden="true">
    <polygon points="0,30 80,30 80,100 0,100 28,65" fill="var(--teal-dark)"/>
    <polygon points="640,30 560,30 560,100 640,100 612,65" fill="var(--teal-dark)"/>
    <polygon points="60,6 580,6 580,86 60,86" fill="var(--teal-bright)"/>
  </svg>
  <div class="title-main abs center">EQUIP YOUR KITCHEN</div>
  <div class="title-for abs center">for</div>
  <div class="title-sub abs center">HEALTHY HOME MEALS</div>
</section>

<section class="why abs">
  <h2 class="why-heading abs center">Why Cook at Home?</h2>
  <p class="why-text abs center">Those who eat out consume an average of 134 calories more per meal.&nbsp; Americans eat out an average of 4.5 times per week, so those extra calories can add up to substantial weight gain -- and give you a reason to prepare your own meals.</p>

  <svg class="chart abs" style="left:120px" width="450" height="440" viewBox="0 0 450 440" aria-label="Excess calories from restaurant meals: about 134 per meal, about 600 per week">
    <g stroke="#e2e2e2" stroke-width="1">
      <line x1="60" y1="20" x2="400" y2="20"/><line x1="60" y1="70" x2="400" y2="70"/>
      <line x1="60" y1="120" x2="400" y2="120"/><line x1="60" y1="170" x2="400" y2="170"/>
      <line x1="60" y1="220" x2="400" y2="220"/><line x1="60" y1="270" x2="400" y2="270"/>
    </g>
    <line x1="60" y1="10" x2="60" y2="320" stroke="#bbb"/>
    <line x1="60" y1="320" x2="400" y2="320" stroke="#bbb"/>
    <g class="chart-label" text-anchor="end">
      <text x="38" y="25">600</text><text x="38" y="75">500</text><text x="38" y="125">400</text>
      <text x="38" y="175">300</text><text x="38" y="225">200</text><text x="38" y="275">100</text>
    </g>
    <rect x="157" y="250" width="26" height="70" fill="var(--green)"/>
    <rect x="264" y="20" width="26" height="300" fill="var(--green)"/>
    <g class="chart-label" text-anchor="middle">
      <text x="170" y="340">Calories per</text><text x="170" y="358">Meal</text>
      <text x="277" y="340">Calories per</text><text x="277" y="358">Week</text>
    </g>
    <polygon points="10,372 440,372 420,397 440,422 10,422 30,397" fill="var(--teal-bright)"/>
    <text class="chart-ribbon-text" x="225" y="403" text-anchor="middle">EXCESS CALORIES FROM RESTAURANT MEALS</text>
  </svg>

  <svg class="chart abs" style="left:640px" width="450" height="440" viewBox="0 0 450 440" aria-label="Pounds gained from restaurant meals: about 3 at 2 months, 4.6 at 6 months, 9 at 1 year">
    <g stroke="#e2e2e2" stroke-width="1">
      <line x1="60" y1="20" x2="400" y2="20"/><line x1="60" y1="70" x2="400" y2="70"/>
      <line x1="60" y1="120" x2="400" y2="120"/><line x1="60" y1="170" x2="400" y2="170"/>
      <line x1="60" y1="220" x2="400" y2="220"/><line x1="60" y1="270" x2="400" y2="270"/>
    </g>
    <line x1="60" y1="10" x2="60" y2="320" stroke="#bbb"/>
    <line x1="60" y1="320" x2="400" y2="320" stroke="#bbb"/>
    <g class="chart-label" text-anchor="end">
      <text x="38" y="25">12</text><text x="38" y="75">10</text><text x="38" y="125">8</text>
      <text x="38" y="175">6</text><text x="38" y="225">4</text><text x="38" y="275">2</text>
    </g>
    <rect x="117" y="245" width="26" height="75" fill="var(--green)"/>
    <rect x="212" y="205" width="26" height="115" fill="var(--green)"/>
    <rect x="307" y="95" width="26" height="225" fill="var(--green)"/>
    <g class="chart-label" text-anchor="middle">
      <text x="130" y="345">2 months</text><text x="225" y="345">6 months</text><text x="320" y="345">1 year</text>
    </g>
    <polygon points="10,372 440,372 420,397 440,422 10,422 30,397" fill="var(--teal-bright)"/>
    <text class="chart-ribbon-text" x="225" y="403" text-anchor="middle">POUNDS GAINED FROM RESTAURANT MEALS</text>
  </svg>
</section>

<h2 class="tools-heading abs center">Make Healthy Eating Easier With These Kitchen Tools</h2>

<!-- column 1 -->
<div class="column abs" style="left:56px">
  <svg class="column-head" width="192" height="322" viewBox="0 0 192 322" aria-hidden="true">
    <polygon points="0,104 96,139 192,104 192,321 0,321" fill="var(--teal-bright)"/>
    <polygon points="0,0 192,0 192,89 96,124 0,89" fill="var(--tab-grey)"/>
    <text class="col-num" x="96" y="80" text-anchor="middle">01</text>
    <text class="col-word" x="96" y="262" text-anchor="middle">PREP</text>
  </svg>
  <div class="tool" style="top:384px"><span class="tool-icon icon-teal" role="img" aria-label="Cutting board icon"></span><div class="tool-name">Cutting Board</div><div class="tool-desc">essential for prepping<br>meat and vegetables</div></div>
  <div class="tool" style="top:636px"><span class="tool-icon icon-teal" role="img" aria-label="Chef's knife icon"></span><div class="tool-name">Chef's Knife</div><div class="tool-desc">go for quality to make<br>chopping, dicing and<br>slicing faster and easier</div></div>
  <div class="tool" style="top:894px"><span class="tool-icon icon-teal" role="img" aria-label="Digital food scale icon"></span><div class="tool-name">Digital Food Scale</div><div class="tool-desc">get the precision you need<br>for perfect recipes and<br>portion control</div></div>
</div>

<!-- column 2 -->
<div class="column abs" style="left:272px">
  <svg class="column-head" width="192" height="322" viewBox="0 0 192 322" aria-hidden="true">
    <polygon points="0,104 96,139 192,104 192,321 0,321" fill="var(--green)"/>
    <polygon points="0,0 192,0 192,89 96,124 0,89" fill="var(--tab-grey)"/>
    <text class="col-num" x="96" y="80" text-anchor="middle">02</text>
    <text class="col-word" x="96" y="262" text-anchor="middle">TECH</text>
  </svg>
  <div class="tool" style="top:384px"><span class="tool-icon icon-green" role="img" aria-label="High-powered blender icon"></span><div class="tool-name">High-Powered Blender</div><div class="tool-desc">make highly nutritious,<br>healthy drinks from fruits<br>and veggies</div></div>
  <div class="tool" style="top:636px"><span class="tool-icon icon-green" role="img" aria-label="Slow cooker icon"></span><div class="tool-name">Slow Cooker</div><div class="tool-desc">cook delicious meals<br>while you are at work</div></div>
  <div class="tool" style="top:894px"><span class="tool-icon icon-green" role="img" aria-label="Pressure cooker icon"></span><div class="tool-name">Pressure Cooker</div><div class="tool-desc">create single pot meals in<br>20 minutes or less</div></div>
</div>

<!-- column 3 -->
<div class="column abs" style="left:488px">
  <svg class="column-head" width="192" height="322" viewBox="0 0 192 322" aria-hidden="true">
    <polygon points="0,104 96,139 192,104 192,321 0,321" fill="var(--teal-bright)"/>
    <polygon points="0,0 192,0 192,89 96,124 0,89" fill="var(--tab-grey)"/>
    <text class="col-num" x="96" y="80" text-anchor="middle">03</text>
    <text class="col-word" x="96" y="262" text-anchor="middle">COOK</text>
  </svg>
  <div class="tool" style="top:384px"><span class="tool-icon icon-teal" role="img" aria-label="Ceramic pan icon"></span><div class="tool-name">Ceramic Pan</div><div class="tool-desc">nonstick cooking surface<br>allows you to cook with-<br>out oil</div></div>
  <div class="tool" style="top:636px"><span class="tool-icon icon-teal" role="img" aria-label="Vegetable steamer icon"></span><div class="tool-name">Vegetable Steamer</div><div class="tool-desc">preserve nutrients and<br>natural, fresh taste</div></div>
  <div class="tool" style="top:894px"><span class="tool-icon icon-teal" role="img" aria-label="Baking sheet icon"></span><div class="tool-name">Baking Sheet</div><div class="tool-desc">ideal for roasting vegeta-<br>bles in the oven or baking<br>chicken and fish dishes</div></div>
</div>

<!-- column 4 -->
<div class="column abs" style="left:704px">
  <svg class="column-head" width="192" height="322" viewBox="0 0 192 322" aria-hidden="true">
    <polygon points="0,104 96,139 192,104 192,321 0,321" fill="var(--green)"/>
    <polygon points="0,0 192,0 192,89 96,124 0,89" fill="var(--tab-grey)"/>
    <text class="col-num" x="96" y="80" text-anchor="middle">04</text>
    <text class="col-word" x="96" y="262" text-anchor="middle">SERVE</text>
  </svg>
  <div class="tool" style="top:384px"><span class="tool-icon icon-green" role="img" aria-label="Cloth napkins icon"></span><div class="tool-name">Cloth Napkins</div><div class="tool-desc">to reduce waste and dress<br>up your table</div></div>
  <div class="tool" style="top:636px"><span class="tool-icon icon-green" role="img" aria-label="Dinnerware icon"></span><div class="tool-name">Dinnerware</div><div class="tool-desc">pre-plate meals rather<br>than serving family style<br>to control portions</div></div>
  <div class="tool" style="top:894px"><span class="tool-icon icon-green" role="img" aria-label="Small plates icon"></span><div class="tool-name">Small Plates</div><div class="tool-desc">use salad plates and<br>smaller dishware to<br>manage perception of<br>food volume</div></div>
</div>

<!-- column 5 -->
<div class="column abs" style="left:920px">
  <svg class="column-head" width="192" height="322" viewBox="0 0 192 322" aria-hidden="true">
    <polygon points="0,104 96,139 192,104 192,321 0,321" fill="var(--teal-bright)"/>
    <polygon points="0,0 192,0 192,89 96,124 0,89" fill="var(--tab-grey)"/>
    <text class="col-num" x="96" y="80" text-anchor="middle">05</text>
    <text class="col-word" x="96" y="262" text-anchor="middle">STORE</text>
  </svg>
  <div class="tool" style="top:384px"><span class="tool-icon icon-teal" role="img" aria-label="Glass storage containers icon"></span><div class="tool-name">Glass Storage Containers</div><div class="tool-desc">keep your healthy left-<br>overs so nothing goes to<br>waste</div></div>
  <div class="tool" style="top:636px"><span class="tool-icon icon-teal" role="img" aria-label="Mason jar icon"></span><div class="tool-name">Mason Jars</div><div class="tool-desc">perfect for premade<br>salads that you can bring<br>to work</div></div>
  <div class="tool" style="top:894px"><span class="tool-icon icon-teal" role="img" aria-label="Freezer bag icon"></span><div class="tool-name">Freezer Safe Re-Sealable<br>Bags</div><div class="tool-desc">prepare double batches to<br>make the most of your<br>time</div></div>
</div>

<section class="contact abs">
  <svg class="contact-ribbon abs" width="640" height="80" viewBox="0 0 640 80" aria-label="FernQuill can help you develop healthier eating habits">
    <polygon points="0,16 40,16 40,70 0,70 16,43" fill="var(--teal-dark)"/>
    <polygon points="640,16 600,16 600,70 640,70 624,43" fill="var(--teal-dark)"/>
    <rect x="22" y="4" width="596" height="56" fill="var(--teal-bright)"/>
    <text class="ribbon-text" x="320" y="40" text-anchor="middle">FernQuill can help you develop healthier eating habits</text>
  </svg>
  <p class="invite abs center">We invite you to learn more. Contact us:</p>
  <div class="brand abs"><span class="brand-dot"></span><span class="brand-name">FernQuill</span></div>
  <p class="site abs center">www.FernQuill.com</p>
</section>

<footer class="sources abs">
  <div><span>Sources:</span>https://www.harvestfacts.org/field-notes/2010/june/eating-out-increases-daily-calorie-intake/</div>
  <div><span></span>https://www.tablerank.com/b/the-state-of-american-dining-in-2016</div>
</footer>

</body>
</html>
```